Speisekarten
Zielgruppe
we run a restaurant and our target groups are families and business people
Aufgabenstellung
The menu consists of a black folder with 8 DIN A4 slots which have a 2 cm border on all sides. The card should be discreet, classy and easy to read without any kind of complicated fonts or pictures. we would like to see creative designs regarding our recommendation at the end of page 3.

```html
<!DOCTYPE html>
<html lang="de">
<head>
<meta charset="utf-8">
<title>Getränkekarte</title>
<link rel="stylesheet" href="https://fonts.googleapis.com/css2?family=Poppins:wght@600;700&display=swap">
<style>
:root{
  --olive:#6b5a2f;
  --sage:#a8aa82;
  --paper:#ffffff;
  --ink:#141414;
}
*{margin:0;padding:0;box-sizing:border-box}
html,body{width:848px;height:1200px;overflow:hidden}
body{background:var(--olive);font-family:"Poppins",sans-serif;color:var(--ink);position:relative}
.backdrop{position:absolute;inset:0;background:var(--olive)}
.sheet{position:absolute;left:47px;top:44px;width:754px;height:1111px;background:var(--paper);border:4px solid var(--sage)}
.frame{position:absolute;left:64px;top:60px;width:718px;height:1076px;border:1.5px solid var(--sage)}
.heading{position:absolute;left:85px;width:678px;display:flex;align-items:center;gap:14px;
  font-weight:700;font-size:19px;letter-spacing:.12em;white-space:nowrap}
.heading::before,.heading::after{content:"";flex:1;border-top:1.3px solid var(--ink)}
.col{position:absolute;font-weight:700;font-size:13.2px;letter-spacing:.08em}
.col.left{left:84px;width:317px}
.col.right{left:443px;width:320px}
.col.wide{left:84px;width:679px}
.row{display:flex;align-items:baseline;height:30px;white-space:nowrap}
.leader{flex:1;border-bottom:1.2px dashed var(--ink);margin:0 2px;transform:translateY(-2px);min-width:8px}
.gap{width:34px;border-bottom:1.2px dashed var(--ink);margin:0 3px;transform:translateY(-2px)}
.gap.s{width:14px}
.size{min-width:38px}
.price{min-width:34px;text-align:right}
.note{font-size:8px;letter-spacing:.06em}
.small{font-size:10.5px}
.info{line-height:17px;font-size:13px}
</style>
</head>
<body>
<div class="backdrop" role="img" aria-label="Olivfarbener Hintergrund mit Muster aus sich überlappenden Kreisbögen"></div>
<div class="sheet"></div>
<div class="frame"></div>

<h2 class="heading" style="top:77px">SOFTGETRÄNKE</h2>
<div class="col left" style="top:108px">
  <div class="row"><span>WASSER</span><span class="gap s"></span><span>0,2L</span><span class="gap s"></span><span>2,90</span><span class="gap s"></span><span>0,75L</span><span class="leader"></span><span class="price">7,50</span></div>
  <div class="row"><span>RIVO COLA</span><span class="leader"></span><span class="size">0,33L</span><span class="gap"></span><span class="price">3,50</span></div>
  <div class="row"><span>COLA LIGHT</span><span class="leader"></span><span class="size">0,33L</span><span class="gap"></span><span class="price">3,50</span></div>
  <div class="row"><span>COLA ZERO</span><span class="leader"></span><span class="size">0,33L</span><span class="gap"></span><span class="price">3,50</span></div>
  <div class="row"><span>LIMO KLAR</span><span class="leader"></span><span class="size">0,33L</span><span class="gap"></span><span class="price">3,50</span></div>
  <div class="row"><span>SONNLIMO</span><span class="leader"></span><span class="size">0,33L</span><span class="gap"></span><span class="price">3,50</span></div>
</div>
<div class="col right" style="top:109px">
  <div class="row"><span>MISTA MIX</span><span class="leader"></span><span class="size">0,33L</span><span class="gap"></span><span class="price">3,50</span></div>
  <div class="row"><span>BITTER LEMON</span><span class="leader"></span><span class="size">0,2L</span><span class="gap"></span><span class="price">3,50</span></div>
  <div class="row"><span>GINGER ALE</span><span class="leader"></span><span class="size">0,2L</span><span class="gap"></span><span class="price">3,50</span></div>
  <div class="row"><span>TONIC WATER</span><span class="leader"></span><span class="size">0,2L</span><span class="gap"></span><span class="price">3,50</span></div>
  <div class="row"><span>WILD BERRY</span><span class="leader"></span><span class="size">0,2L</span><span class="gap"></span><span class="price">3,50</span></div>
  <div class="row"><span>DOUGH</span><span class="leader"></span><span class="size">0,33L</span><span class="gap"></span><span class="price">3,50</span></div>
</div>

<h2 class="heading" style="top:309px">SÄFTE</h2>
<div class="col left" style="top:351px">
  <div class="row"><span>MANGOSAFT</span><span class="leader"></span><span class="size">0,2L</span><span class="gap"></span><span class="price">3,50</span></div>
  <div class="row"><span>RHABARBERSAFT</span><span class="leader"></span><span class="size">0,2L</span><span class="gap"></span><span class="price">3,50</span></div>
  <div class="row"><span>JOHANNISBEERENSAFT</span><span class="leader"></span><span class="size">0,2L</span><span class="gap"></span><span class="price">3,50</span></div>
  <div class="row"><span>ORANGENSAFT</span><span class="leader"></span><span class="size">0,2L</span><span class="gap"></span><span class="price">3,50</span></div>
  <div class="row"><span>ANANASSAFT</span><span class="leader"></span><span class="size">0,2L</span><span class="gap"></span><span class="price">3,50</span></div>
  <div class="row"><span>MULTIVITAMIN</span><span class="leader"></span><span class="size">0,2L</span><span class="gap"></span><span class="price">3,50</span></div>
  <div class="row"><span>KIRSCHNEKTAR</span><span class="leader"></span><span class="size">0,2L</span><span class="gap"></span><span class="price">3,50</span></div>
</div>
<div class="col right" style="top:353px">
  <div class="row"><span>BANANENNEKTAR</span><span class="leader"></span><span class="size">0,2L</span><span class="gap"></span><span class="price">3,50</span></div>
  <div class="row"><span>MARACUJANEKTAR</span><span class="leader"></span><span class="size">0,2L</span><span class="gap"></span><span class="price">3,50</span></div>
  <div class="row"><span>KIBA</span><span class="gap"></span><span>0,2L</span><span class="gap s"></span><span>2,90</span><span class="gap s"></span><span class="size">0,4L</span><span class="gap"></span><span class="price">7,50</span></div>
  <div class="row"><span>APFELSCHORLE QUELLGUT</span><span class="leader"></span><span class="size">0,3L</span><span class="gap"></span><span class="price">3,50</span></div>
  <div class="row"><span>TOMATENSAFT</span><span class="leader"></span><span class="size">0,2L</span><span class="gap"></span><span class="price">3,50</span></div>
  <div class="row"><span>SAFTSCHORLE</span><span class="leader"></span><span class="size">0,2L</span><span class="gap"></span><span class="price">3,50</span></div>
  <div class="row"><span>SAFTSCHORLE</span><span class="leader"></span><span class="size">0,4L</span><span class="gap"></span><span class="price">5,00</span></div>
</div>

<h2 class="heading" style="top:580px">WARME GETRÄNKE</h2>
<div class="col left" style="top:624px;width:318px">
  <div class="row" style="height:28px"><span>SCHWARZER TEE KLEIN</span><span class="note">(AUFGESETZT)</span><span class="leader"></span><span class="price">2,50</span></div>
  <div class="row" style="height:30px"><span>SCHWARZER TEE GROß</span><span class="note">(AUFGESETZT)</span><span class="leader"></span><span class="price">4,00</span></div>
  <div class="row" style="height:24px"><span class="small">FRISCHER PFEFFERMINZTEE</span><span class="leader"></span><span class="price">4,50</span></div>
  <div class="row" style="height:28px"><span class="small">FRISCHER PFEFFERMINZTEE MIT INGWER</span><span class="leader"></span><span class="price">5,00</span></div>
  <div class="row" style="height:27px"><span>GRÜNER TEE/KAMILLENTEE</span><span class="leader"></span><span class="price">4,00</span></div>
  <div class="row" style="height:31px"><span>LOSER TEE (NACHVOLL)</span><span class="leader"></span><span class="price">5,00</span></div>
  <div class="row" style="height:26px"><span>ESPRESSO</span><span class="leader"></span><span class="price">2,50</span></div>
  <div class="row"><span>DOPPELTER ESPRESSO</span><span class="leader"></span><span class="price">3,50</span></div>
</div>
<div class="col right" style="top:624px;width:317px">
  <div class="row" style="height:28px"><span>KAFFEE</span><span class="leader"></span><span class="price">2,90</span></div>
  <div class="row" style="height:30px"><span>MILCHKAFFEE</span><span class="leader"></span><span class="price">3,80</span></div>
  <div class="row" style="height:25px"><span>CAPPUCCINO</span><span class="leader"></span><span class="price">3,80</span></div>
  <div class="row" style="height:29px"><span>LATTE MACCHIATO</span><span class="leader"></span><span class="price">3,80</span></div>
  <div class="row" style="height:46px"><span>ESPRESSO MACCHIATO</span><span class="leader"></span><span class="price">2,70</span></div>
  <div class="info">MILCHHALTIGE GETRÄNKE WAHLWEISE<br>MIT (AUFPREIS) LAKTOSEFREI MILCH</div>
  <div class="row" style="height:18px"><span>HAFERMILCH</span><span class="leader"></span><span class="price">0,80</span></div>
</div>

<h2 class="heading" style="top:862px">FLASCHENBIERE (TALGRUND)</h2>
<div class="col wide" style="top:906px">
  <div class="row" style="height:29px"><span>TALGRUND PILS / TALGRUND ALKOHOLFREI</span><span class="leader"></span><span class="size" style="width:44px">0,33L</span><span class="gap"></span><span class="price">3,50</span></div>
  <div class="row" style="height:29px"><span>RADLER / RADLER ALKOHOLFREI</span><span class="leader"></span><span class="size" style="width:44px">0,33L</span><span class="gap"></span><span class="price">3,50</span></div>
  <div class="row" style="height:29px"><span>WEIZEN / HELL / DUNKEL / ALKOHOLFREI</span><span class="leader"></span><span class="size" style="width:44px">0,5L</span><span class="gap"></span><span class="price">3,50</span></div>
</div>

<h2 class="heading" style="top:1014px">LONGDRINKS</h2>
<div class="col left" style="top:1044px">
  <div class="row" style="height:26px"><span>VODKA (NORDLICHT) LEMON</span><span class="leader"></span><span class="price">9,00</span></div>
  <div class="row" style="height:26px"><span>VODKA (NORDLICHT) VOLT ENERGY</span><span class="leader"></span><span class="price">9,50</span></div>
  <div class="row" style="height:26px"><span>WHISKEY (OLD HARROW) COLA</span><span class="leader"></span><span class="price">9,50</span></div>
</div>
<div class="col right" style="top:1044px">
  <div class="row" style="height:26px"><span>MARLOW TONIC</span><span class="leader"></span><span class="price">9,00</span></div>
  <div class="row" style="height:26px"><span>ASHBY TONIC</span><span class="leader"></span><span class="price">10,50</span></div>
  <div class="row" style="height:26px"><span>CARIBO COLA</span><span class="leader"></span><span class="price">9,00</span></div>
</div>
</body>
</html>
```